Placing my newer logo on my existing business card

I have a business card that I had you guys do years ago, then I changed my logo, I love both my business card and my logo. The challenge is both my logo and my business card are very similar in color. So I'm not sure how to make my logo stand out.

Sick

```html
<!DOCTYPE html>
<html lang="en">
<head>
<meta charset="utf-8">
<title>Vital Balance Clinic – Business Cards</title>
<link rel="stylesheet" href="https://fonts.googleapis.com/css2?family=Open+Sans:wght@400;600&family=Cormorant+Garamond:wght@500&family=Great+Vibes&display=swap">
<style>
  :root{
    --backdrop:#959595;
    --paper:#ffffff;
    --rust:#ad4a2e;
    --teal:#6f8d8f;
    --teal-soft:#9fb4b6;
    --ink:#2b2b2b;
    --ink-soft:#3a3a3a;
    --muted:#8a9a9b;
    --white:#ffffff;
  }
  *{box-sizing:border-box;margin:0;padding:0}
  html,body{width:1200px;height:1000px;overflow:hidden;background:var(--backdrop)}
  body{position:relative;font-family:"Open Sans",Arial,sans-serif;color:var(--ink)}

  .card{position:absolute;width:578px;height:333px;border-radius:16px;overflow:hidden;background:var(--paper)}
  .card--front{left:12px;top:157px}
  .card--back{left:607px;top:157px}
  .card--services{left:12px;top:511px;background:var(--teal);color:var(--white)}
  .card--appointment{left:607px;top:511px}

  .brand{position:absolute;display:flex;flex-direction:column;align-items:center;text-align:center}
  .brand__dot{width:46px;height:46px;border-radius:50%;background:var(--teal-soft);margin-bottom:12px}
  .brand__name{font-family:"Open Sans",Arial,sans-serif;font-weight:600;color:var(--rust);font-size:19px;line-height:1.2;white-space:nowrap}

  .contact{position:absolute;text-align:center;font-size:14px;line-height:18px;color:var(--ink-soft)}
  .icons{display:flex;justify-content:center;gap:3px;margin-bottom:6px}
  .rule{width:78px;height:1px;background:var(--rust);margin:10px auto 7px}

  .card--front .brand{left:0;width:310px;top:38px}
  .person{position:absolute;left:0;width:310px;top:142px;text-align:center}
  .person__name{font-weight:600;font-size:16px;color:var(--ink)}
  .person__role{font-family:"Cormorant Garamond",Georgia,serif;font-size:12px;letter-spacing:2px;color:var(--muted);margin-top:2px}
  .card--front .contact{left:0;width:310px;top:188px}
  .photo{position:absolute;left:288px;top:0;width:290px;height:333px;
    background:linear-gradient(90deg,#ffffff 0%,#e9ddd2 22%,#cdb5a2 55%,#b9a08c 100%)}

  .card--back .brand{left:0;width:316px;top:62px}
  .card--back .contact{left:0;width:316px;top:168px;font-size:16px;line-height:20px}
  .watermark{position:absolute;right:-90px;top:-20px;width:420px;height:420px;border-radius:50%;background:#eef2f2}

  .services__title{position:absolute;left:29px;top:16px;font-size:23.5px;font-weight:600}
  .services__list{position:absolute;top:58px;list-style:none;font-size:16.5px;line-height:22.8px;color:#f3f6f6}
  .services__list li::before{content:"• "}
  .services__list--left{left:29px}
  .services__list--right{left:323px}
  .services__divider{position:absolute;left:29px;right:29px;top:269px;height:1px;background:#c3d1d2}
  .services__brand{position:absolute;left:70px;top:281px;display:flex;align-items:center;gap:8px}
  .services__brand .brand__dot{width:30px;height:30px;margin:0;background:#e8eeee}
  .services__brand .brand__name{color:var(--white);font-size:15px;text-align:left}
  .services__call{position:absolute;right:30px;top:281px;text-align:right}
  .services__phone{font-size:17.5px}
  .services__phone b{font-weight:600}
  .services__web{font-size:12px;font-weight:600;margin-top:1px}

  .card--appointment .brand{left:0;width:578px;top:20px}
  .card--appointment .brand__dot{width:40px;height:40px;margin-bottom:10px}
  .appointment__title{position:absolute;left:0;width:578px;top:136px;text-align:center;font-family:"Cormorant Garamond",Georgia,serif;font-weight:500;font-size:27px;letter-spacing:6px;color:var(--ink)}
  .appointment__fields{position:absolute;left:67px;top:224px;display:flex;align-items:flex-end;font-family:"Cormorant Garamond",Georgia,serif;font-size:17px;color:var(--ink)}
  .appointment__line{display:inline-block;width:172px;border-bottom:1px solid var(--rust);margin:0 5px 4px 4px}
  .appointment__tagline{position:absolute;left:0;width:578px;top:268px;text-align:center;font-family:"Great Vibes",cursive;font-size:38px;color:var(--ink)}
</style>
</head>
<body>

<svg width="0" height="0" style="position:absolute">
  <defs>
    <symbol id="icon-phone" viewBox="0 0 32 32">
      <circle cx="16" cy="16" r="16" fill="#ad4a2e"/>
      <path d="M11.5 8.5c.8-.4 1.6 0 2 .8l1.3 2.8c.3.7.1 1.5-.5 1.9l-1.1.8c.9 2 2.5 3.7 4.5 4.6l.8-1.1c.5-.6 1.3-.8 2-.5l2.8 1.3c.8.4 1.2 1.2.8 2l-.6 1.4c-.4 1-1.5 1.6-2.6 1.4-5.5-1-9.9-5.4-10.9-10.9-.2-1.1.4-2.2 1.4-2.6z" fill="#fff"/>
    </symbol>
    <symbol id="icon-globe" viewBox="0 0 32 32">
      <circle cx="16" cy="16" r="16" fill="#ad4a2e"/>
      <g fill="none" stroke="#fff" stroke-width="1.4">
        <circle cx="16" cy="16" r="8"/>
        <ellipse cx="16" cy="16" rx="3.5" ry="8"/>
        <path d="M8 16h16M9.2 12h13.6M9.2 20h13.6"/>
      </g>
    </symbol>
  </defs>
</svg>

<section class="card card--front">
  <div class="photo" role="img" aria-label="Portrait photograph of the clinic director in a white jacket against a brick wall"></div>
  <div class="brand">
    <span class="brand__dot"></span>
    <span class="brand__name">Vital Balance Clinic</span>
  </div>
  <div class="person">
    <div class="person__name">Marissa Calloway-Hale</div>
    <div class="person__role">DIRECTOR</div>
  </div>
  <div class="contact">
    <div class="icons">
      <svg width="25" height="25"><use href="#icon-phone"/></svg>
      <svg width="25" height="25"><use href="#icon-globe"/></svg>
    </div>
    555-014-2277<br>vitalbalanceclinic.com
    <div class="rule"></div>
    1452 Ridge Ave<br>Northfield, UT 84000
  </div>
</section>

<section class="card card--back">
  <div class="watermark"></div>
  <div class="brand">
    <span class="brand__dot"></span>
    <span class="brand__name">Vital Balance Clinic</span>
  </div>
  <div class="contact">
    <div class="icons">
      <svg width="32" height="32"><use href="#icon-phone"/></svg>
      <svg width="32" height="32"><use href="#icon-globe"/></svg>
    </div>
    555-014-2277<br>vitalbalanceclinic.com
    <div class="rule"></div>
    1452 Ridge Ave<br>Northfield, UT 84000
  </div>
</section>

<section class="card card--services">
  <h2 class="services__title">Does your Doctor Say, your Labs are Normal?</h2>
  <ul class="services__list services__list--left">
    <li>GLP-1 Injections</li>
    <li>Medications</li>
    <li>Unexplained weight gain</li>
    <li>Insulin Resistanc Diabetes (1&amp;2)</li>
    <li>Pcos (polycistic ovarian symdrom)</li>
    <li>PMS &amp; PMDD</li>
    <li>Cystic Acne</li>
    <li>Head Aches &amp; Migraines</li>
    <li>Chronic Fatigue</li>
  </ul>
  <ul class="services__list services__list--right">
    <li>Low Testosterone &amp; E.D.</li>
    <li>Arthritis &amp; Chronic Pain</li>
    <li>Hypothyroid</li>
    <li>Under-active Thyroid</li>
    <li>Fybromyalgia</li>
    <li>Autoimmune Diseases</li>
    <li>All Menopausal Symptoms</li>
    <li>Hysterectomies</li>
    <li>Osteoporosis</li>
  </ul>
  <div class="services__divider"></div>
  <div class="services__brand">
    <span class="brand__dot"></span>
    <span class="brand__name">Vital Balance Clinic</span>
  </div>
  <div class="services__call">
    <div class="services__phone"><b>Call Today!</b> (555) 014-2277</div>
    <div class="services__web">vitalbalanceclinic.com</div>
  </div>
</section>

<section class="card card--appointment">
  <div class="brand">
    <span class="brand__dot"></span>
    <span class="brand__name">Vital Balance Clinic</span>
  </div>
  <div class="appointment__title">APPOINTMENT ON...</div>
  <div class="appointment__fields">
    TIME:<span class="appointment__line"></span>DATE:<span class="appointment__line"></span>
  </div>
  <div class="appointment__tagline">Let's Make it Happen</div>
</section>

</body>
</html>
```